Makeup brushes and lashes brochure for vibrant new brand!

(UPDATE we have added a sample brochure for your guidance. Similar layout required,brush description is not necessary in lengthy form,brush number and title is acceptable))We are looking for an enthusiastic designer to work with us on our new 3fold brochure of our products. The brochure will be included in customers orders to entice them to make more purchases. All products must be displayed in along witglh the product name/ numbers.

We have three product ranges,makeup brushes,false lashes and cosmetic sponge. The brochure should tie in with our other packaging themes and be clear and modern.

The following information is required:

Company description-
Established in 2015 by Professional Makeup Artist Maura Delaney, Dab&Glow is one of Irelands leading cosmetic brands. We provide the beauty industry with incredibly high quality makeup brushes and Luxury Lashes.
Expertly design by Maura and handmade using incredibly high quality natural and synthetic hair.

Brush Care-(To be placed after brush imagery and descriptions.)

Keep'em clean! To keep your brushes in their best shape possible,clean them once a week with warm soapy water. Avoid submerging the ferrule Metal part) in water as this could loosen the glue inside and cause the hair to shed. Shedding is normal for the first few washes.
Rinse the brush well with clean water and air dry flat.

Lash Care-( To be placed after lash imagery and descriptions.)

All our lashes are re-usable so take care of them and you will have fluttery long lashes for up to 30 wears!

We recommend cleaning your lashes after every 3 wears.

Firstly, remove any left over glue from the lash band and soak the lashes in warm soapy water for 5 minutes. Remove and rinse and residue from the lash. re-Shape and Replace the lash back into its case and let dry naturally. As good as new!

Brushes descriptions- (Please crop brush images to below logo on handle.)

BRUSH SETS

Quite Rosy Glow - Containing 8 professional brushes,this set is your go to for your everyday makeup application. DG01,DG02 , DG03,DG04,DG05,DG06,DG10,DG24

Top Lids Set- Contain 8 of our incredible eye brushes for expert application. DG02,DG06,DG12,DG14,DG16,DG18,DG20,DG24

Sharp Cheek set- The ideal mix containing 6 of our most popular face and eye brushes. DG07,DG09,DG14,DG16,DG18,DG24.

INDIVIDUAL BRUSHES

DG01- Large synthetic powder brush. Ideal for use with powder foundations,creams or liquids.

DG02- Ideal for detailed eye work, Using ultra soft hair ,it won't irritate the delicate eye area.

DG03- Domed Shape,synthetic hair, the DG03 is perfect for seamlessly buffing liquid,creams,gel based foundations into the skin for a flawless finish.

DG04- Ultra soft synthetic hair,DG04 is a must have multi task brush. From concealer to eyeshadow application this all rounder is essential in the makeup bag.

DG05- Silky soft blush brush applies the perfect amount of product for flawless skin.

DG06- Precisely blends shadows into the socket of the eye for controlled blending.

DG08- NEW!(BOLD Writing) Domed shadow blending brush,ideal for softening edges.

DG09- The unique tapered shape on our contour is perfect for chiseling out cheekbones or simply adding a pop of colour to the cheeks using the flat sides. (Synthetic)

DG10- Synthetic hair,DG10 is ultra thin with a precise angle ,ideal for creating winged eyeliner or definition to brows.

DG12- Our finest blending brush yet! This truly is a must have for anyone who loves to add precise detail to their makeup looks. Super soft and light, it blends with ease for a flawless finish.

DG14- This is the ultimate brush for under eye blending! Dense, silky and sturdy, it is simply an essential in any eye look.

DG16- Another must have for any makeup bag is our flat shading brush. No more fall out from eyeshadows as this controls the placement perfectly.( Synthetic)

DG18- If your looking to pack on colour to a specific area or to smudge out for a smokey effect this nifty little brush is one for the collection.(Synthetic)

DG20- An all rounder brush, our flat definer is a real multitasker. From defining the brows to cutting the crease there is no job too big or too small for the DG20. (Synthetic)

DG24- Ultra soft and dense. Hand crafted ,tapered hair blends shadows effortlessly.

LASHES
3 lash ranges-
VelTrim-
Luxury meets glamour. Each lash is designed to give your peepers that beautiful full lash look with added volume and glamour. Made from silk fibres and a flexible cotton band,you'll love the comfort!

Aurora -
Our lightest lash range yet! Made from ethically soured human hair,each lash oozes femininity and natural volume. You wont feel like your wearing lashes at all!

DewPoint Sponge-

Our innovative design makes blending creams or liquids a dream! Just dampen your sponge and apply your product to the skin. We recommend using the round side in bouncing motions to blend foundation and the flat side to push the product into the skin. The pointed end is specifically designed to get into those hard to reach areas,under eye area,around the nose etc.

Sponge cleaning instructions-( To be placed after lash imagery and descriptions.)

We recommend replacing your sponge every 6weeks. To clean your DewPoint Sponge,soak the sponge in hot soapy water and rinse until all makeup has been removed. Squeeze out excess water and allow to dry flat in a well ventilated room.

Information for end of brochure-
Visit www.dabandglow.example for prices and more information on all products.

Social media icons-
Facebook
Instagram
twitter

Choice of several brand logo jpeg and png.
Any further questions,we are happy to answer them.

Target Market(s)

Young,women

Industry/Entity Type

Hair And Beauty

Font styles to use
Other font styles liked:
• GeoSans Light

Colors
ecdaeb
eea4c8
e667a6
e34298
a64599
b868aa
000000
ffffff

Requirements
Must have
• Vibrant colour,sleek flow throughout brochure.
Should not have
• Images of people.

```html
<!DOCTYPE html>
<html lang="en">
<head>
<meta charset="utf-8">
<title>Dab&amp;Glow Brochure – Outside</title>
<link href="https://fonts.googleapis.com/css2?family=Quicksand:wght@400;500;600&family=Great+Vibes&display=swap" rel="stylesheet">
<style>
  :root {
    --pink-pale: #ecdaeb;
    --pink-soft: #eea4c8;
    --pink: #e667a6;
    --pink-hot: #e34298;
    --purple: #a64599;
    --purple-soft: #b868aa;
    --plum-deep: #5e1a55;
    --ink: #000000;
    --paper: #ffffff;
    --stage: #eef0f3;
  }
  * { box-sizing: border-box; margin: 0; padding: 0; }
  html, body { width: 850px; height: 1200px; overflow: hidden; }
  body {
    background: var(--stage);
    font-family: "Quicksand", sans-serif;
    color: var(--paper);
  }
  .spread {
    position: absolute;
    left: 20px; top: 295px;
    width: 810px; height: 610px;
    background: linear-gradient(180deg, #0d060c 0%, #2a0c27 45%, var(--plum-deep) 100%);
    overflow: hidden;
    box-shadow: 0 10px 30px rgba(0,0,0,.18);
  }
  .panel { position: absolute; top: 0; width: 270px; height: 610px; }
  .panel--brushes { left: 0; }
  .panel--about { left: 270px; }
  .panel--cover { left: 540px; }
  .fold { position: absolute; top: 0; width: 1px; height: 610px; background: rgba(255,255,255,.05); }
  .fold--one { left: 270px; } .fold--two { left: 540px; }

  .curves { position: absolute; inset: 0; width: 810px; height: 610px; }

  /* brush list */
  .brush-list { position: absolute; left: 45px; top: 128px; width: 190px; list-style: none; }
  .brush { display: flex; flex-direction: column; align-items: center; margin-bottom: 7px; }
  .brush__image {
    height: var(--h); width: 170px; border-radius: 3px 8px 8px 3px;
    background: linear-gradient(90deg, #d9cfc6 0%, #6c5c53 30%, #c8c8cc 38%, var(--pink-hot) 42%, var(--pink) 100%);
  }
  .brush__name { font-size: 6.5px; margin-top: 4px; color: var(--pink-pale); }

  .care { position: absolute; left: 20px; top: 495px; width: 225px; text-align: center; }
  .care__title { color: var(--pink); font-size: 10px; font-weight: 500; margin-bottom: 8px; }
  .care__text { font-size: 7.2px; line-height: 1.3; }

  /* about panel */
  .wordmark {
    font-family: "Quicksand", sans-serif; font-weight: 400;
    color: var(--pink); letter-spacing: 1px;
  }
  .panel--about .wordmark { position: absolute; left: 52px; top: 205px; font-size: 34px; }
  .about { position: absolute; left: 25px; top: 295px; width: 205px; }
  .about__title { color: var(--pink); font-size: 10.5px; font-weight: 500; margin-bottom: 9px; }
  .about__text { font-size: 7.4px; line-height: 1.3; text-align: justify; }
  .promise { margin-top: 30px; font-size: 12.5px; line-height: 1.2; }
  .accent { color: var(--pink); }
  .visit { margin-top: 28px; font-size: 9.5px; }
  .visit__line--small { font-size: 9px; color: var(--pink); }
  .visit__line--caps { font-size: 11px; color: var(--pink); }
  .globe { vertical-align: -2px; }
  .follow { position: absolute; left: 25px; top: 536px; font-size: 8.5px; display: flex; align-items: center; gap: 4px; }
  .follow__dot { width: 9px; height: 9px; border-radius: 50%; background: var(--paper); }
  .follow__dot:first-of-type { margin-left: 4px; }

  /* cover panel */
  .panel--cover .wordmark { position: absolute; right: 22px; top: 62px; font-size: 34px; }
  .model {
    position: absolute; left: 20px; top: 160px; width: 230px; height: 320px;
    border-radius: 45% 45% 10px 10px;
    background: radial-gradient(ellipse at 50% 40%, #e8c49a 0%, #b98455 45%, rgba(94,26,85,0) 78%);
  }
  .tagline { position: absolute; left: 0; top: 518px; width: 270px; text-align: center; color: #4a1c44; }
  .tagline__script { font-family: "Great Vibes", cursive; font-size: 27px; color: var(--pink-hot); line-height: 1; }
  .tagline__sub { font-size: 12px; font-weight: 600; letter-spacing: .3px; }
  .tagline__web { margin-top: 8px; font-size: 6.5px; letter-spacing: 2px; color: #777; border-top: 1px solid #ddd; display: inline-block; padding-top: 4px; }
</style>
</head>
<body>
<main class="spread">
  <svg class="curves" viewBox="0 0 810 610" aria-hidden="true">
    <path d="M0 0 H210 Q70 40 0 170 Z" fill="var(--paper)"/>
    <path d="M0 180 Q60 40 220 0" fill="none" stroke="var(--pink-hot)" stroke-width="5"/>
    <path d="M0 190 Q55 50 230 0" fill="none" stroke="var(--pink-soft)" stroke-width="1.5"/>
  </svg>

  <section class="panel panel--brushes">
    <ul class="brush-list">
      <li class="brush"><div class="brush__image" style="--h:8px" role="img" aria-label="Angled liner brush"></div><span class="brush__name">DG10 Angled liner brush</span></li>
      <li class="brush"><div class="brush__image" style="--h:10px" role="img" aria-label="Large tapered blending brush"></div><span class="brush__name">DG24 Large Tapered Blending brush</span></li>
      <li class="brush"><div class="brush__image" style="--h:12px" role="img" aria-label="Small blending brush"></div><span class="brush__name">DG06 Small blending brush</span></li>
      <li class="brush"><div class="brush__image" style="--h:24px" role="img" aria-label="Angled blush brush"></div><span class="brush__name">DG05 Angled blush brush</span></li>
      <li class="brush"><div class="brush__image" style="--h:10px" role="img" aria-label="Round buffer brush"></div><span class="brush__name">DG04 Round buffer brush</span></li>
      <li class="brush"><div class="brush__image" style="--h:28px" role="img" aria-label="Round foundation brush"></div><span class="brush__name">DG03 Round foundation brush</span></li>
      <li class="brush"><div class="brush__image" style="--h:8px" role="img" aria-label="Small pencil brush"></div><span class="brush__name">DG02 Small pencil brush</span></li>
      <li class="brush"><div class="brush__image" style="--h:34px" role="img" aria-label="Large dense powder brush"></div><span class="brush__name">DG01 Large dense powder brush</span></li>
    </ul>
    <div class="care">
      <h2 class="care__title">Brush Care</h2>
      <p class="care__text">Keep'em clean! To keep your brushes in their best shape possible, clean them once a week with warm soapy water. Avoid submerging the ferrule (Metal part) in water as this could loosen the glue inside and cause the hair to shed. Shedding is normal for the first few washes. Rinse the brush well with clean water and air dry flat.</p>
    </div>
  </section>

  <section class="panel panel--about">
    <div class="wordmark">Dab&amp;Glow</div>
    <div class="about">
      <h2 class="about__title">Company description</h2>
      <p class="about__text">Established in 2015 by Professional Makeup Artist Maura Delaney, Dab&amp;Glow is one of Irelands leading cosmetic brands. We provide the beauty industry with incredibly high quality makeup brushes and Luxury Lashes.</p>
      <p class="promise"><span class="accent">Expertly design</span> by<br>Maura and handmade<br>using <span class="accent">incredibly high quality</span><br>natural and synthetic hair.</p>
      <div class="visit">
        <p>Visit <svg class="globe" width="10" height="10" viewBox="0 0 10 10"><circle cx="5" cy="5" r="4.3" fill="none" stroke="#fff" stroke-width=".9"/><ellipse cx="5" cy="5" rx="1.8" ry="4.3" fill="none" stroke="#fff" stroke-width=".7"/><line x1=".7" y1="5" x2="9.3" y2="5" stroke="#fff" stroke-width=".7"/></svg> www.dabandglow.example</p>
        <p class="visit__line--small">for prices and more information</p>
        <p class="visit__line--caps">on ALL PRODUCTS</p>
      </div>
    </div>
    <div class="follow">FOLLOW US ON <span class="follow__dot"></span><span class="follow__dot"></span><span class="follow__dot"></span></div>
  </section>

  <section class="panel panel--cover">
    <div class="wordmark">Dab&amp;Glow</div>
    <div class="model" role="img" aria-label="Portrait photograph of a model with long golden curls"></div>
    <svg class="curves" viewBox="0 0 270 610" style="width:270px" aria-hidden="true">
      <path d="M0 610 V560 Q70 470 270 455 V610 Z" fill="var(--paper)"/>
      <path d="M0 555 Q70 465 270 450" fill="none" stroke="var(--pink-hot)" stroke-width="4"/>
    </svg>
    <div class="tagline">
      <p class="tagline__script">Professional, Vibrant</p>
      <p class="tagline__sub">&amp; Modern Makeup Brushes</p>
      <p class="tagline__web">WWW.DABANDGLOW.EXAMPLE</p>
    </div>
  </section>

  <span class="fold fold--one"></span><span class="fold fold--two"></span>
</main>
</body>
</html>
```